Book cover: Stormy Days Survival for Kids (A5)

I have a book called Stormy Days Survival for Teens. It is a book for teenagers which gives them tips and tactics on how to survive life's challenges regarding friends, family, feelings, relationships and hard stuff in life generally. I will upload the cover of this book but you can see it on my past jobs as one of the designers her eon Pixel Bazaar did it for me.
I have a new book I've written called Stormy Days Survival for Kids. This is a parallel book to Stormy Days Survival for Teens, but it is specifically for 8 to 12 or 13 year olds, rather than for older teens.
A very important aspect of this job is that it SHOULD MATCH in some strong way - the Stormy Days Survival for Teens book. I will be selling them together, displaying them together and I want them to look like two of a pair. It might be that you use the same image as the first book but change the colour of the image so that it is bright orange and green perhaps? Or that there is another image but in the image is placed in the exact same position across the book as the first book. It needs to look like the books are by the same author.
However, I would like this one to look a bit "younger", more kid friendly. For example, a font that looks like it is for kids, or kids' writing perhaps.
I dont want to have photos on the book, and I dont think I want cartoons or drawings - because I'm not sure how this will tie in with the first book.
I want it to look modern, fresh and designed specifically for kids. The text needs to be:
Stormy Days Survival - For Kids!
Tips and ideas for 8 to 13 year olds about how to stay cool, calm and confident on even the toughest days!
The back cover is going to mostly just have the table of contents listed and a blurb, with one or two cartoons which I will supply. I am keen to pick a designer to just do the front cover first and will ask them to do the back cover later.
UPDATED: I have attached three files with fonts that I like.

```html
<!DOCTYPE html>
<html lang="en">
<head>
<meta charset="utf-8">
<title>Stormy Days Survival for Kids – Book Cover</title>
<link rel="stylesheet" href="https://fonts.googleapis.com/css2?family=Gochi+Hand&family=Short+Stack&family=Arimo:wght@400&display=swap">
<style>
  :root{
    --backdrop:#8fa4a4;
    --paper:#ffffff;
    --ink:#111111;
    --red:#e8231f;
    --green:#5fdc1e;
    --blue:#3fb6dc;
    --yellow:#f4e62a;
    --charcoal:#2b2b2b;
  }
  *{box-sizing:border-box;margin:0;padding:0}
  html,body{width:1200px;height:1000px;overflow:hidden;background:var(--backdrop)}
  .spread{position:relative;width:1200px;height:1000px}
  .page{position:absolute;top:108px;width:553px;height:782px;background:var(--paper);overflow:hidden}
  .back{left:41px}
  .front{left:608px}

  .title{font-family:"Gochi Hand",cursive;color:var(--ink);text-transform:uppercase;text-align:center;letter-spacing:1px;white-space:nowrap}
  .back .title{position:absolute;top:60px;left:0;width:100%;font-size:33px;line-height:1}
  .front .title{position:absolute;top:50px;left:0;width:100%;font-size:46px;line-height:1.12}

  .blurb{position:absolute;top:114px;left:61px;width:440px;font-family:"Arimo",Arial,sans-serif;font-size:10.2px;line-height:1.25;color:var(--ink)}
  .blurb h2{font-family:"Short Stack",cursive;font-weight:400;font-size:15px;line-height:1;margin:4px 0 4px}
  .blurb p{margin-bottom:8px}
  .blurb p.tight{margin-bottom:0}
  .h-kids{color:var(--red)}
  .h-parents{color:var(--green)}
  .h-about{color:var(--blue)}
  .blurb h3{font-family:"Short Stack",cursive;font-weight:400;font-size:10px;color:var(--red);margin:16px 0 8px}

  .smiley-field{position:absolute;background:radial-gradient(circle at 45% 60%,var(--charcoal) 0 14%,transparent 15%),linear-gradient(100deg,var(--green) 0%,var(--blue) 20%,var(--red) 40%,var(--yellow) 55%,var(--blue) 70%,var(--green) 85%,var(--red) 100%)}
  .back .smiley-field{left:0;top:558px;width:553px;height:157px}
  .front .smiley-field{left:0;top:200px;width:553px;height:345px}

  .tagline{position:absolute;top:560px;left:0;width:100%;text-align:center;font-family:"Short Stack",cursive;font-size:17px;line-height:1.35;color:var(--ink)}
  .t-red{color:var(--red)}
  .t-green{color:var(--green)}
  .t-blue{color:var(--blue)}

  .author{position:absolute;top:660px;right:62px;text-align:right}
  .author-name{font-family:"Gochi Hand",cursive;font-size:38px;line-height:1;color:var(--ink);letter-spacing:1px}
  .author-role{font-family:"Arimo",Arial,sans-serif;font-size:15px;color:var(--ink);margin-top:6px;margin-right:22px}
</style>
</head>
<body>
<main class="spread">

  <section class="page back">
    <h1 class="title">Stormy Days Survival for Kids</h1>
    <div class="blurb">
      <h2 class="h-kids">Kids:</h2>
      <p>Sometimes life really sucks.</p>
      <p>Things go wrong with friends (you feel lonely, left out, have a fight or are getting bullied).</p>
      <p>Things go wrong with family (your parents make you do boring stuff, don't let you do things, your siblings make you mad).</p>
      <p class="tight">Things go wrong with life (you can't sleep, someone you love died, your parents are splitting up).</p>
      <p>And sometimes you just feel sad, worried a lot or really, really mad.</p>
      <p class="tight">This book has stories about real kids who have feelings and problems just like you.</p>
      <p class="tight">It has ideas about what you can say to get help. And it has tips about what you can do</p>
      <p>to help you cope with feeling bad and going through tough times.</p>
      <h2 class="h-parents">Parents:</h2>
      <p>This book will help your 8 - 13 year old child know they are normal, increase their resilience and teach them how to cope - calmly and confidently with all life throws at them. They can read it themselves or you can read it with them and talk about it.</p>
      <h2 class="h-about">About Maren:</h2>
      <p>Maren is a clinical psychologist specialising in working with kids and teens. She has worked with hundreds of families over the last 20 years and presents seminars to schools across Australia.</p>
      <h3>Praise for Maren's previous book: Stormy Days Survival for Teens:</h3>
      <p>“Incredibly insightful, intelligent and relevant” (Odette, Parent).</p>
      <p>“Bravo! Practical, Readable and helpful” (Clara Vossen, Teacher)</p>
      <p>“Loved it. Know I'm not alone. Very, very helpful” (Fern, Teen)</p>
    </div>
    <div class="smiley-field" role="img" aria-label="Crowd of glossy coloured emoji balls in red, green, blue and yellow with one dark sad ball in the middle"></div>
  </section>

  <section class="page front">
    <h1 class="title">Stormy Days Survival<br>For Kids</h1>
    <div class="smiley-field" role="img" aria-label="Close-up crowd of glossy coloured emoji balls in red, green, blue and yellow with one dark sad ball in the middle"></div>
    <p class="tagline">Ideas and tips for when you feel <span class="t-red">mad</span>, <span class="t-green">worried</span><br>or <span class="t-blue">sad</span> - or when life goes <span class="t-red">horribly wrong!</span></p>
    <div class="author">
      <div class="author-name">Maren Tolley</div>
      <div class="author-role">clinical psychologist</div>
    </div>
  </section>

</main>
</body>
</html>
```